Anzeigengestaltung für Beratungsunternehmen
Zielgruppe
Firmenname: BETRIEBSKOMPASS.ORG | Beratung in den Bereichen: Arbeitssicherheit, Brandschutz und Gefahrgut | Zielgruppe: Unternehmen, die Beratung zu obigen Themen suchen | Meine Qualifikationen: Fachkraft für Arbeitssicherheit, Gefahrgut- und Brandschutzbeauftragter, Sachkundiger nach ChemVerbotsV, Ausbilder für Flurförderzeuge, Krane, Hubarbeitsbühnen und Brandschutzhelfer (auch die Ausbilder-Themen könnten erscheinen/hervorgehoben werden - ich biete dafür Kurse an)
Aufgabenstellung
Es soll für Werbung in Zeitschriften und auch für Werbebanner geeignet sein. Vielleicht in 16:9?! Mal hochkant, mal quer.

```html
<!DOCTYPE html>
<html lang="de">
<head>
<meta charset="utf-8">
<title>Betriebskompass – Beratung Arbeitssicherheit, Brandschutz, Gefahrgut</title>
<link rel="stylesheet" href="https://fonts.googleapis.com/css2?family=Barlow+Condensed:wght@400;600;700&family=Montserrat:wght@500&display=swap">
<style>
  :root {
    --backdrop: #c9cdd5;
    --paper: #ffffff;
    --blue-top: #1a6083;
    --blue-bottom: #1b4864;
    --brand-red: #b80e24;
    --heading-grey: #444444;
    --body-grey: #333333;
    --photo-yellow: #e9c12a;
    --photo-orange: #e76a2c;
    --photo-grey: #cfd3d6;
  }
  html, body {
    margin: 0;
    padding: 0;
    width: 1200px;
    height: 1117px;
    overflow: hidden;
    background: var(--backdrop);
  }
  .ad {
    position: absolute;
    left: 311px;
    top: 44px;
    width: 579px;
    height: 1029px;
    background: var(--paper);
  }
  .ad-art {
    position: absolute;
    inset: 0;
    display: block;
  }
  .headline { font-family: "Barlow Condensed", sans-serif; font-weight: 700; fill: var(--paper); }
  .subline { font-family: "Barlow Condensed", sans-serif; font-weight: 400; fill: var(--paper); }
  .brand-name { font-family: "Barlow Condensed", sans-serif; font-weight: 700; fill: var(--heading-grey); }
  .qual-heading { font-family: "Barlow Condensed", sans-serif; font-weight: 700; fill: var(--heading-grey); }
  .qual-item { font-family: "Montserrat", sans-serif; font-weight: 500; fill: var(--body-grey); font-size: 16px; }
  .tick-ring { fill: none; stroke: var(--brand-red); stroke-width: 2.2; }
  .tick-mark { fill: none; stroke: var(--brand-red); stroke-width: 3; stroke-linecap: round; stroke-linejoin: round; }
  .web-address { font-family: "Barlow Condensed", sans-serif; font-weight: 700; fill: var(--paper); font-size: 30px; }
</style>
</head>
<body>
<main class="ad">
  <svg class="ad-art" viewBox="0 0 579 1029" width="579" height="1029">
    <defs>
      <linearGradient id="blue-band-fill" x1="0" y1="0" x2="0" y2="1">
        <stop offset="0.55" stop-color="var(--blue-top)"/>
        <stop offset="1" stop-color="var(--blue-bottom)"/>
      </linearGradient>
      <linearGradient id="site-photo-fill" x1="0" y1="0" x2="1" y2="0">
        <stop offset="0" stop-color="var(--photo-yellow)"/>
        <stop offset="0.35" stop-color="#d9dc7a"/>
        <stop offset="0.6" stop-color="var(--photo-orange)"/>
        <stop offset="1" stop-color="var(--photo-grey)"/>
      </linearGradient>
      <linearGradient id="portrait-fill" x1="0" y1="0" x2="0" y2="1">
        <stop offset="0" stop-color="#8a6f5c"/>
        <stop offset="0.45" stop-color="#d9b8a2"/>
        <stop offset="1" stop-color="#1f2a44"/>
      </linearGradient>
    </defs>

    <!-- Site photo area -->
    <path d="M0,563 Q289.5,441 579,563 L579,739 L0,739 Z" fill="url(#site-photo-fill)"
          role="img" aria-label="Foto: Arbeitsschutz-Besprechung mit gelbem Schutzhelm und Warnwesten"/>

    <!-- Blue band -->
    <path class="blue-band" d="M0,96 Q289.5,214 579,96 L579,563 Q289.5,441 0,563 Z" fill="url(#blue-band-fill)"/>

    <!-- Brand mark -->
    <g class="brand">
      <circle cx="289.5" cy="122" r="97" fill="var(--paper)"/>
      <text class="brand-name" x="289.5" y="128" text-anchor="middle" font-size="19">BETRIEBSKOMPASS.ORG</text>
    </g>

    <!-- Headline -->
    <text class="headline" x="289.5" y="306" text-anchor="middle" font-size="90" textLength="390" lengthAdjust="spacingAndGlyphs">BERATUNG IN</text>
    <text class="headline" x="289.5" y="386" text-anchor="middle" font-size="90" textLength="467" lengthAdjust="spacingAndGlyphs">DEN BEREICHEN</text>
    <text class="subline" x="289.5" y="430" text-anchor="middle" font-size="36" textLength="441" lengthAdjust="spacingAndGlyphs">ARBEITSSICHERHEIT, BRANDSCHUTZ</text>
    <text class="subline" x="289.5" y="469" text-anchor="middle" font-size="36" textLength="202" lengthAdjust="spacingAndGlyphs">UND GEFAHRGUT</text>

    <!-- Consultant portrait -->
    <path class="portrait" d="M424,683 L579,683 L579,970 L338,970 L424,896 Z" fill="url(#portrait-fill)"
          role="img" aria-label="Porträtfoto des Beraters im dunklen Anzug"/>

    <!-- Qualifications -->
    <text class="qual-heading" x="51" y="788" font-size="34" textLength="287" lengthAdjust="spacingAndGlyphs">MEINE QUALIFIKATIONEN:</text>
    <g class="qual-list">
      <g transform="translate(59,810)"><circle class="tick-ring" r="8"/><path class="tick-mark" d="M-4,0 L-1,4 L7,-6"/></g>
      <text class="qual-item" x="80" y="816">Fachkraft für Arbeitssicherheit</text>
      <g transform="translate(59,836)"><circle class="tick-ring" r="8"/><path class="tick-mark" d="M-4,0 L-1,4 L7,-6"/></g>
      <text class="qual-item" x="80" y="842" textLength="332" lengthAdjust="spacingAndGlyphs">Gefahrgut- und Brandschutzbeauftragter</text>
      <g transform="translate(59,863)"><circle class="tick-ring" r="8"/><path class="tick-mark" d="M-4,0 L-1,4 L7,-6"/></g>
      <text class="qual-item" x="80" y="869">Sachkundiger nach ChemVerbotsV</text>
      <g transform="translate(59,889)"><circle class="tick-ring" r="8"/><path class="tick-mark" d="M-4,0 L-1,4 L7,-6"/></g>
      <text class="qual-item" x="80" y="895">Ausbilder für Flurförderzeuge, Krane</text>
      <g transform="translate(59,916)"><circle class="tick-ring" r="8"/><path class="tick-mark" d="M-4,0 L-1,4 L7,-6"/></g>
      <text class="qual-item" x="80" y="922">Hubarbeitsbühnen und</text>
      <text class="qual-item" x="80" y="943">Brandschutzhelfer</text>
    </g>

    <!-- Footer -->
    <rect class="footer-band" x="0" y="970" width="579" height="59" fill="var(--brand-red)"/>
    <text class="web-address" x="289.5" y="1010" text-anchor="middle" textLength="461" lengthAdjust="spacing">WWW.BETRIEBSKOMPASS.ORG</text>
  </svg>
</main>
</body>
</html>
```